Webdesign für Zirkeltraining für Frauen
Zielgruppe
zirkeltraining für Frauen.
Frauen jeden Alters ... 18-85 Jahre.
Aufgabenstellung
Bitte in den Farben der Bilder und der Logos bleiben. Klare Struktur. Logo wird gerade vom designer Final bearbeitet und liegt daher nur als Beispiel dem Briefing bei.

```html
<!DOCTYPE html>
<html lang="de">
<head>
<meta charset="utf-8">
<title>LUMAFIT – Kontakt</title>
<link href="https://fonts.googleapis.com/css2?family=Montserrat:ital,wght@0,400;0,500;0,600;1,400&display=swap" rel="stylesheet">
<style>
:root{
  --brand:#23a9dc;
  --ink:#111;
  --muted:#555;
  --map-a:#e9ebee;
  --map-b:#d9e8d8;
  --white:#fff;
}
*{margin:0;padding:0;box-sizing:border-box}
html,body{width:1200px;height:1168px;overflow:hidden;background:var(--white)}
body{font-family:"Montserrat",sans-serif;color:var(--ink);position:relative}
.header{position:absolute;top:0;left:0;width:1200px;height:55px;background:var(--white)}
.brand{position:absolute;left:44px;top:15px;font-size:20px;font-weight:400;letter-spacing:6px;color:var(--ink)}
.nav a{position:absolute;top:18px;font-size:15px;color:var(--ink);text-decoration:none}
.social span{position:absolute;width:8px;height:8px;border:1.3px solid #444;border-radius:50%}
.map{position:absolute;top:55px;left:0;width:1200px;height:366px;background:linear-gradient(100deg,var(--map-a) 0%,var(--map-a) 62%,var(--map-b) 80%,var(--map-a) 100%)}
h2{position:absolute;left:0;width:1200px;text-align:center;font-weight:500;font-size:27px}
.info{position:absolute;top:505px;width:300px;text-align:center}
.info svg{display:block;margin:0 auto;height:40px}
.info h3{font-weight:500;font-size:25px;margin-top:14px}
.info p{font-size:14px;line-height:21px;margin-top:4px}
.info p.left{display:inline-block;text-align:left}
.label{position:absolute;font-size:10px;color:var(--muted)}
.field{position:absolute;border:1px solid var(--brand);font-size:8px;color:var(--brand);padding:0 12px;display:flex;align-items:center;background:var(--white)}
.field.area{align-items:flex-start;padding-top:12px;color:#9fd3ec}
.field.name{color:#7cc6e8}
.alert{position:absolute;right:12px;top:10px;width:10px;height:10px;border-radius:50%;background:var(--brand);color:#fff;font-size:7px;text-align:center;line-height:10px;font-weight:600}
.submit{position:absolute;left:487px;top:896px;width:204px;height:30px;background:var(--brand);color:#fff;font-size:10px;font-weight:600;display:flex;align-items:center;justify-content:center}
.submit svg{position:absolute;right:14px;top:10px}
.footer{position:absolute;top:1003px;left:0;width:1200px;height:165px;background:var(--brand);color:#fff}
.col{position:absolute;top:40px;width:150px}
.col h4{font-size:13px;font-weight:600;line-height:15px;margin-bottom:16px}
.col p{font-size:11px;line-height:12px}
.col.italic p{font-style:italic}
.footer .social span{border-color:#fff;top:48px}
</style>
</head>
<body>
<header class="header">
  <div class="brand">LUMAFIT</div>
  <nav class="nav">
    <a style="left:271px" href="#">Startseite</a>
    <a style="left:396px" href="#">Trainingskonzept</a>
    <a style="left:580px" href="#">Mitgliedschaften</a>
    <a style="left:753px" href="#">Aktuelles</a>
    <a style="left:869px" href="#">Kontakt</a>
  </nav>
  <div class="social">
    <span style="left:1034px;top:24px"></span>
    <span style="left:1063px;top:24px"></span>
    <span style="left:1090px;top:24px"></span>
    <span style="left:1119px;top:24px"></span>
  </div>
</header>

<div class="map" role="img" aria-label="Stadtplan mit Standortmarkierung des Studios"></div>

<h2 style="top:438px">Komm uns einfach besuchen</h2>

<div class="info" style="left:169px">
  <svg viewBox="0 0 40 40" width="40"><path d="M38 2 2 18l14 5 5 15Z M38 2 16 23" fill="none" stroke="#111" stroke-width="2.5" stroke-linejoin="round"/></svg>
  <h3>Mail</h3>
  <p>hallo@lumafit-studio.de</p>
</div>
<div class="info" style="left:450px">
  <svg viewBox="0 0 40 40" width="40"><path d="M20 39C14 26 8 22 8 13a12 12 0 0 1 24 0c0 9-6 13-12 26Z" fill="none" stroke="#111" stroke-width="2.5"/><path d="M12 20c3 5 13 5 16 0L20 38Z" fill="#111"/></svg>
  <h3>Adresse</h3>
  <p class="left">Lindenweg 12<br>99999 Musterstadt</p>
</div>
<div class="info" style="left:724px">
  <svg viewBox="0 0 40 40" width="40"><path d="M1 9C12 1 28 1 39 9l-4 4c-9-6-21-6-30 0Z" fill="#111"/><g fill="#111"><circle cx="14" cy="16" r="2"/><circle cx="20" cy="16" r="2"/><circle cx="26" cy="16" r="2"/><circle cx="14" cy="22" r="2"/><circle cx="20" cy="22" r="2"/><circle cx="26" cy="22" r="2"/><circle cx="14" cy="28" r="2"/><circle cx="20" cy="28" r="2"/><circle cx="26" cy="28" r="2"/><circle cx="20" cy="35" r="2"/></g></svg>
  <h3>Telefon</h3>
  <p>+49 0555 123456</p>
</div>

<h2 style="top:710px">Oder schreib uns eine Nachricht</h2>

<form>
  <div class="label" style="left:271px;top:776px">Name:</div>
  <div class="field name" style="left:271px;top:792px;width:225px;height:31px">Required Field</div>
  <div class="label" style="left:271px;top:830px">Mail:</div>
  <div class="field" style="left:271px;top:845px;width:225px;height:31px">error@mail.com<span class="alert">!</span></div>
  <div class="label" style="left:548px;top:776px">Message:</div>
  <div class="field area" style="left:548px;top:792px;width:382px;height:84px">Type something…</div>
  <div class="submit">Absenden<svg width="12" height="10" viewBox="0 0 12 10"><path d="M0 5h10M6 1l4 4-4 4" fill="none" stroke="#fff" stroke-width="1.5"/></svg></div>
</form>

<footer class="footer">
  <div class="col" style="left:354px">
    <h4>Kontakt</h4>
    <p>+49 0555 123456<br>hallo@lumafit-studio.de<br>Lindenweg 12<br>99999 Musterstadt</p>
  </div>
  <div class="col italic" style="left:542px">
    <h4>Sitelinks</h4>
    <p>Das Trainingskonzept<br>Unsere Mitgliedschaften<br>Unser Blog<br>Was ist Zirkeltraining</p>
  </div>
  <div class="col" style="left:745px">
    <h4 style="margin-bottom:16px">Informationen /<br>Aktuelles</h4>
    <p>Blogbeitrag 1<br>Blogbeitrag 2<br>Blogbeitrag 3<br>Blogbeitrag 4</p>
  </div>
  <div class="social">
    <span style="left:1120px"></span>
    <span style="left:1142px"></span>
    <span style="left:1162px"></span>
  </div>
</footer>
</body>
</html>
```